automatic Real Estate Sales Brochure

Print-out of 3 to 8 pages automatically on a color inkjet printer. Page size A4
All details for my Real Estate Sales Design Project are in attached file.
Here some points:
We have abound 100 real estate objects for sale (houses, flats and pieces of land).
For each item, our system creates automatically a sales documentation, which we print out and hand to the potential buyers after they've visited the object or send it by mail upon request in form of a pdf.
This document should be of 3 to maximum 8 pages.
It should be of a modern design and invite the client to read it.
The information should be clear and quick to find.
If the global look could somehow relate to the look of our web site www.velorancasa.ch, that would be nice.
The company data is there for legal reasons, but it is the agent's phone and mail that the clients should use for contact.
The photos should be of big size (2 by page?) without being distorted nor cut.
Optionally, to save ink and pages, maybe only the first 3-4 photos full size and the rest smaller?

Target Market(s)

will be printed or sent as PDF "on the fly", meaning no pre-printing at a print shop!

Industry/Entity Type

Real Estate

Font styles to use
Sans Serif

Requirements
Must have
• see details in attached file
Should not have
• no edge-to-edge printing
• no double-page printing (A3)

```html
<!DOCTYPE html>
<html lang="fr">
<head>
<meta charset="utf-8">
<title>Brochure de vente – velorancasa</title>
<link rel="stylesheet" href="https://fonts.googleapis.com/css2?family=Lato:wght@400;700&family=Oswald:wght@500;600&display=swap">
<style>
:root{
  --red:#e8222a;
  --grey:#5e5f5d;
  --ink:#2f2f2f;
  --text:#3a3a3a;
  --paper:#ffffff;
  --backdrop:#e8e5e1;
}
*{margin:0;padding:0;box-sizing:border-box}
html,body{width:1200px;height:1200px;overflow:hidden}
body{background:var(--backdrop);font-family:'Lato',sans-serif;color:var(--text);position:relative}
.page{position:absolute;top:234px;width:529px;height:742px;background:var(--paper);box-shadow:0 4px 14px rgba(0,0,0,.25);overflow:hidden}
.page--front{left:48px}
.page--inside{left:623px}
.abs{position:absolute}
.band-red{left:0;top:0;width:386px;background:var(--red)}
.band-grey{left:386px;top:0;right:0;background:var(--grey)}
.page--front .band-red,.page--front .band-grey{height:50px}
.page--inside .band-red,.page--inside .band-grey{height:45px}
.brand{display:flex;align-items:center;gap:7px;font-family:'Oswald',sans-serif;font-weight:600;color:var(--grey);letter-spacing:.5px}
.brand__mark{width:14px;height:14px;background:var(--red)}
.page--front .brand{left:0;right:0;top:70px;justify-content:center;font-size:34px}
.page--inside .brand{left:22px;top:66px;font-size:25px}
.page--inside .brand__mark{width:11px;height:11px}
.photo{display:block}
.rule{background:var(--red)}
.headline{font-family:'Oswald',sans-serif;font-weight:600;text-transform:uppercase}
.tagline{left:0;right:0;top:554px;text-align:center;font-size:19px;color:var(--ink);letter-spacing:.3px}
.tagline em{font-style:normal;color:var(--red)}
.front-title{left:250px;width:270px;text-align:center}
.front-title__line{top:616px;font-size:22px;color:var(--ink);font-weight:400}
.front-title__strong{top:640px;font-size:24px;color:var(--red)}
.front-meta{top:677px;font-size:12.5px;color:var(--grey)}
.front-meta .sep{color:var(--red);margin:0 8px;font-weight:700}
.contact-bar{background:var(--grey);color:#fff;display:flex;align-items:center;gap:18px;font-size:12px}
.contact-bar span{display:flex;align-items:center;gap:5px}
.contact-bar svg{width:12px;height:12px;fill:none;stroke:#fff;stroke-width:1.6}
.page--front .contact-bar{left:198px;right:0;top:698px;height:32px;justify-content:center}
.page--inside .contact-bar{left:0;right:0;top:708px;height:24px;padding-left:24px;font-size:9.5px;gap:14px}
.page--inside .contact-bar svg{width:10px;height:10px}
.inside-title{left:23px;top:120px;font-size:20px;color:var(--red)}
.inside-title-strong{left:23px;top:148px;font-size:22px;color:var(--ink);letter-spacing:.4px}
.section-label{left:23px;top:190px;font-size:14px;color:var(--red)}
.body-copy{font-size:9.2px;line-height:12px;text-align:justify;color:var(--text)}
.desc{left:23px;top:208px;width:263px}
.desc p+p{margin-top:6px;text-align:left}
.details{left:30px;top:528px;width:485px}
.details .lead{font-size:11.5px;line-height:14px;color:var(--ink);margin-bottom:4px;text-align:left;width:370px}
.details p{margin-bottom:7px}
</style>
</head>
<body>

<section class="page page--front">
  <div class="abs band-red"></div>
  <div class="abs band-grey"></div>
  <div class="abs brand"><span class="brand__mark"></span>velorancasa</div>

  <div class="abs photo" style="left:10px;top:132px;width:505px;height:392px;background:linear-gradient(to bottom,#ebe8df 0%,#ebe8df 10%,#9fd0ef 14%,#c8e6f5 38%,#4f7a3a 55%,#3d6a2f 78%,#2c3f25 100%)" role="img" aria-label="Vue depuis le balcon sur un jardin arboré"></div>

  <div class="abs rule" style="left:250px;top:538px;width:266px;height:8px"></div>
  <div class="abs headline tagline">Specialiste romand de <em>la vente immobiliere</em></div>

  <div class="abs photo" style="left:22px;top:604px;width:164px;height:128px;background:linear-gradient(160deg,#c0141a,#7a0d10 60%,#4a0709)" role="img" aria-label="Jardin de la résidence, teinté rouge"></div>

  <div class="abs front-title front-title__line">Lumineux 4.5 de 100m2</div>
  <div class="abs headline front-title front-title__strong">Idealement situe</div>
  <div class="abs front-title front-meta">1200 Genève<span class="sep">|</span>Reference : 2447</div>

  <div class="abs contact-bar">
    <span><svg viewBox="0 0 12 12"><path d="M2 1.5l2 0 1 3-1.3 1a6 6 0 0 0 2.8 2.8l1-1.3 3 1v2c0 .5-.5 1-1 1A9.5 9.5 0 0 1 1 2.5c0-.5.5-1 1-1z"/></svg>21 555 01 47</span>
    <span><svg viewBox="0 0 12 12"><circle cx="6" cy="6" r="5"/><path d="M1 6h10M6 1c2.5 3 2.5 7 0 10M6 1c-2.5 3-2.5 7 0 10"/></svg>www.velorancasa.ch</span>
  </div>
</section>

<section class="page page--inside">
  <div class="abs band-red"></div>
  <div class="abs band-grey"></div>
  <div class="abs brand"><span class="brand__mark"></span>velorancasa</div>

  <div class="abs inside-title">Lumineux 4.5 de 100m2</div>
  <div class="abs headline inside-title-strong">Idealement situe</div>
  <div class="abs headline section-label">Description</div>
  <div class="abs body-copy desc">
    <p>Venez visiter sans tarder ce bel appartement situé dans un environnement idyllique, calme et vert tout en étant proche du centre ville et de toutes les commodités. Il profite de beaux volumes et de pieces de vie tres lumineuses. Au 1er étage d'une copropriété soignée, c'est le bien ideal pour un couple ou une famille</p>
    <p>Cet appartement pourrait aussi convenir comme investissement pour un client souhaitant le louer.</p>
  </div>

  <div class="abs photo" style="left:322px;top:86px;width:181px;height:216px;background:linear-gradient(to bottom,#f2efec,#d8d0ca 55%,#2a2522)" role="img" aria-label="Portrait de la conseillère immobilière"></div>

  <div class="abs rule" style="left:26px;top:318px;width:230px;height:6px"></div>

  <div class="abs photo" style="left:23px;top:336px;width:374px;height:178px;background:linear-gradient(to bottom,#e8e1d6 0%,#ddd6cb 50%,#b8743a 62%,#c98a45 85%,#a8612a 100%)" role="img" aria-label="Séjour lumineux avec parquet et baies vitrées"></div>

  <div class="abs body-copy details">
    <p class="lead">Est en bon état d'entretien et se réjouit d'accueillir ses nouveaux Clara Moretti propriétaires</p>
    <p class="lead">Se distribue ainsi :</p>
    <p>Une entrée avec armoire encastrée desserre de part et d'autre la partie jour et la partie nuit. La spacieuse piece de vie se compose d'une cuisine ouverte entiérement équipée et aménagée s'ouvrant sur le séjour. Il profite d'une exposition optimale. Du séjour, vous avez acces a un agréable balcon qui offre une belle vue dégagée sur un environnement verdoyant.</p>
    <p>La partie nuit offre trois belles chambres, une salle de bains avec baignoire, lavabo, wc ainsi qu' un wc visiteurs.</p>
    <p>Deux places de parc intérieures en sus s'ajoutent à ce bel appartement</p>
    <p>N'hésitez pas, contactez-moi pour plus d'informations et pour une visite</p>
  </div>

  <div class="abs contact-bar">
    <span><svg viewBox="0 0 12 12"><path d="M2 1.5l2 0 1 3-1.3 1a6 6 0 0 0 2.8 2.8l1-1.3 3 1v2c0 .5-.5 1-1 1A9.5 9.5 0 0 1 1 2.5c0-.5.5-1 1-1z"/></svg>21 555 01 47</span>
    <span><svg viewBox="0 0 12 12"><circle cx="6" cy="6" r="5"/><path d="M1 6h10M6 1c2.5 3 2.5 7 0 10M6 1c-2.5 3-2.5 7 0 10"/></svg>www.velorancasa.ch</span>
    <span><svg viewBox="0 0 12 12"><rect x="1" y="2.5" width="10" height="7"/><path d="M1 2.5l5 4 5-4"/></svg>info@velorancasa.ch</span>
    <span><svg viewBox="0 0 12 12"><path d="M6 11s-3.5-4-3.5-6.5a3.5 3.5 0 0 1 7 0C9.5 7 6 11 6 11z"/><circle cx="6" cy="4.5" r="1.2"/></svg>Rue des Tilleuls 7, 1804 Corsier</span>
  </div>
</section>

</body>
</html>
```